Brisk Rig Vitals: Truck Smoke Check Company

I need a logo for a truck health company in California called "Brisk Rig Vitals". This company does smoke checks for heavy duty diesel trucks under the Pacific Clean Skies Council (PCSC) called HD I/M tests. I want the brand to feel reliable.

Target Market(s)

California Diesel Trucks. Individual truck drivers and trucking companies.

Industry/Entity Type

Automotive

Contact Information for Business Card

Company Name, Slogan, contact information. marcotellez@briskrigvitals-example.com

```html
<!DOCTYPE html>
<html lang="en">
<head>
<meta charset="utf-8">
<title>Brisk Rig Vitals — Business Card</title>
<link href="https://fonts.googleapis.com/css2?family=Jost:ital,wght@0,400;0,500;0,800;1,500;1,700&family=Open+Sans:wght@500&display=swap" rel="stylesheet">
<style>
  :root {
    --navy: #26246a;
    --navy-band: #2c3766;
    --lavender: #8d93b8;
    --white: #ffffff;
    --ink: #1c1c2a;
    --orange: #f5a11a;
    --backdrop: #e9e6e1;
  }
  * { margin: 0; padding: 0; box-sizing: border-box; }
  html, body { width: 1200px; height: 675px; overflow: hidden; }
  body {
    background: var(--backdrop);
    display: flex; align-items: center; justify-content: center; gap: 50px;
    font-family: "Jost", sans-serif;
  }
  .card {
    position: relative; width: 540px; height: 310px; border-radius: 28px;
    overflow: hidden; box-shadow: 0 10px 28px rgba(0,0,0,.18);
  }

  /* Front */
  .card--front {
    background: var(--navy); color: var(--white);
    display: flex; flex-direction: column; align-items: center; justify-content: center;
  }
  .brand { display: flex; align-items: center; gap: 14px; }
  .brand__mark { width: 30px; height: 30px; background: currentColor; }
  .brand__name { font-weight: 800; font-size: 52px; line-height: 1; letter-spacing: -.5px; }
  .tagline { font-weight: 400; font-size: 19px; margin-top: 12px; letter-spacing: .3px; }

  /* Back */
  .card--back { background: var(--white); color: var(--navy); }
  .back__bands { position: absolute; inset: 0; }
  .back__brand { position: absolute; top: 38px; right: 40px; text-align: right; }
  .back__brand .brand { justify-content: flex-end; gap: 9px; }
  .back__brand .brand__mark { width: 16px; height: 16px; }
  .back__brand .brand__name { font-size: 29px; }
  .back__brand .tagline { font-size: 10px; margin-top: 5px; color: var(--navy); }
  .divider {
    position: absolute; top: 132px; left: 185px; width: 320px; height: 1px; background: var(--ink);
  }
  .website {
    position: absolute; top: 146px; right: 38px;
    font-family: "Open Sans", sans-serif; font-weight: 500; font-size: 14px; color: var(--orange);
  }
  .person { position: absolute; left: 34px; top: 110px; }
  .person__name { font-style: italic; font-weight: 700; font-size: 30px; line-height: 1; }
  .person__role { font-style: italic; font-weight: 500; font-size: 10px; color: var(--ink); margin-top: 3px; }
  .contacts { list-style: none; margin-top: 16px; font-family: "Open Sans", sans-serif; font-size: 12px; color: var(--ink); }
  .contacts li { display: flex; align-items: center; gap: 9px; margin-bottom: 7px; }
  .contacts svg { width: 17px; height: 17px; flex: none; }
</style>
</head>
<body>

<section class="card card--front">
  <div class="brand">
    <span class="brand__mark"></span>
    <span class="brand__name">Brisk Rig Vitals</span>
  </div>
  <p class="tagline">Reliable Smoke Checks, Stronger Compliance.</p>
</section>

<section class="card card--back">
  <svg class="back__bands" viewBox="0 0 540 310" preserveAspectRatio="none" aria-hidden="true">
    <polygon points="455,180 540,95 540,310 395,310" fill="var(--navy-band)"/>
    <polygon points="440,200 450,190 388,310 345,310" fill="var(--lavender)"/>
  </svg>

  <div class="back__brand">
    <div class="brand">
      <span class="brand__mark"></span>
      <span class="brand__name">Brisk Rig Vitals</span>
    </div>
    <p class="tagline">Reliable Smoke Checks, Stronger Compliance.</p>
  </div>

  <div class="divider"></div>
  <p class="website">www.briskrigvitals-example.com</p>

  <div class="person">
    <h1 class="person__name">MY NAME</h1>
    <p class="person__role">Founder &amp; Director</p>
    <ul class="contacts">
      <li>
        <svg viewBox="0 0 20 20"><circle cx="10" cy="10" r="9" fill="none" stroke="var(--ink)" stroke-width="1.3"/><path d="M7 5.5l1.6 2.4-1 1c.6 1.2 1.5 2.1 2.7 2.7l1-1 2.4 1.6-.9 1.6c-3.5-.3-6.3-3.1-6.6-6.6z" fill="var(--ink)"/></svg>
        555 201 7734
      </li>
      <li>
        <svg viewBox="0 0 20 20"><circle cx="10" cy="10" r="9" fill="none" stroke="var(--ink)" stroke-width="1.3"/><rect x="7" y="5" width="6" height="10" rx="1" fill="none" stroke="var(--ink)" stroke-width="1.3"/></svg>
        555 318 4402
      </li>
      <li>
        <svg viewBox="0 0 20 20"><circle cx="10" cy="10" r="9" fill="none" stroke="var(--ink)" stroke-width="1.3"/><rect x="5.5" y="6.5" width="9" height="7" fill="var(--ink)"/><path d="M5.5 6.5l4.5 4 4.5-4" fill="none" stroke="var(--white)" stroke-width="1"/></svg>
        marcotellez@briskrigvitals-example.com
      </li>
    </ul>
  </div>
</section>

</body>
</html>
```